Killer Webpage Design

I currently have a self-hosted webpage through wordpress at www.vantrelmedia.com - the content is complete and I'm happy with this but I need it designed (no coding) to complete my requirements. I'm happy to take designs which are non-Wordpress if there is specific advantage in this.

My full branding logos are attached along with color files. My main aim is consistent branding across all areas (social media, business cards, emails, websites). I have the rest running but am not happy with the available default selections from Wordpress.

I would prefer to use the darker blue version of the logo as I feel this has more standout in online media, however I would appreciate submissions with both variants to help me choose.

With the homepage I will also want to see blog pages and category pages designed but this can come after I have selected a design to go with,

Sites that I like and are related to my business include the following:
http://www.plumora.com/au/accounting-software/
http://www.taskgriddle.com/home.aspx
https://brimtill.com/register
Updates

Apologies for the confusion - to clarify for designers I am looking for design only, no coding.

FYI - i have now uploaded business cards for an idea of the contemporary style of design completed so far.

Target Market(s)

small to medium business. Not systemised but looking for help and support.

Industry/Entity Type

Business

Requirements
Must have
• I'm looking for a minimalist professional page, with the ability to easily add new sections when required. I will also need a CMS to add blog posts on the go, with the same features that it currently has (comments, social logon etc)

```html
<!DOCTYPE html>
<html lang="en">
<head>
<meta charset="utf-8">
<title>Vantrel Media</title>
<link href="https://fonts.googleapis.com/css2?family=Exo+2:wght@300;400;600;700;800&display=swap" rel="stylesheet">
<style>
:root{
  --navy:#1a5a78;
  --blue:#17709a;
  --blue-light:#1d82ad;
  --teal:#2aa3b3;
  --red:#a31f2c;
  --orange:#f07f37;
  --orange-dark:#f26a10;
  --text:#2c5a74;
  --muted:#9aa6ad;
  --white:#ffffff;
}
*{margin:0;padding:0;box-sizing:border-box}
html,body{width:1200px;height:1006px;overflow:hidden;background:var(--white)}
body{font-family:"Exo 2",sans-serif;color:var(--text);position:relative}
.page{position:relative;width:1200px;height:1006px;overflow:hidden}

/* header */
.site-header{position:absolute;top:0;left:0;width:1200px;height:75px;background:linear-gradient(#fff,#f1f3f4)}
.brand{position:absolute;left:196px;top:22px;display:flex;align-items:center;gap:8px}
.brand-dot{width:30px;height:30px;border-radius:50%;background:var(--teal)}
.brand-name{font-size:24px;font-weight:600;color:var(--navy)}
.social{position:absolute;left:730px;top:15px;display:flex;gap:3px}
.social span{width:20px;height:20px;border-radius:50%;background:var(--navy)}
.search{position:absolute;left:815px;top:14px;display:flex;height:22px}
.search-field{width:136px;border:1px solid #ccd3d7;border-radius:3px 0 0 3px;background:#fff;font-size:8px;color:#b6bec3;padding:6px 0 0 26px;letter-spacing:.5px}
.search-btn{width:46px;background:var(--navy);color:#fff;font-size:8px;font-weight:700;border-radius:0 11px 11px 0;text-align:center;line-height:22px}
.main-nav{position:absolute;right:204px;top:48px;display:flex;align-items:center;font-size:12.5px;font-weight:600;color:var(--navy)}
.main-nav a{color:inherit;text-decoration:none;padding:0 8px;border-left:1px dotted #9bb}
.main-nav a:first-child{border:0}
.main-nav .active{background:var(--navy);color:#fff;border-radius:11px;padding:5px 16px;font-size:11px;font-weight:700;margin-right:6px}

/* hero */
.hero{position:absolute;top:75px;left:0;width:1200px;height:400px;background:radial-gradient(ellipse at 30% 30%,var(--blue-light),var(--blue) 55%,#0f5b80)}
.hero-title{position:absolute;left:197px;top:82px;font-size:26px;line-height:33px;color:#fff;font-weight:300;letter-spacing:-1.2px;white-space:nowrap;z-index:2}
.hero-title strong{font-weight:800}
.hero-text{position:absolute;left:197px;top:172px;width:370px;font-size:11px;line-height:13.5px;color:#e2eef4;font-weight:300}
.hero-actions{position:absolute;left:195px;top:255px;display:flex;gap:5px}
.btn{background:linear-gradient(var(--orange),var(--orange-dark));color:#fff;font-size:15px;font-weight:300;padding:8px 12px;border-radius:3px;letter-spacing:-.3px}
.hero-photo{position:absolute;left:715px;top:4px;width:245px;height:360px;background:linear-gradient(#2b3036,#1c1f24);border-radius:100px 100px 0 0}
.hero-curve{position:absolute;left:0;bottom:0}

/* services */
.services-head{position:absolute;top:462px;left:0;width:1200px;text-align:center}
.services-head .rule{position:absolute;top:15px;left:0;width:1200px;border-top:1px dotted #c6cfd3}
.services-title{position:relative;display:inline-block;background:#fff;padding:0 6px;font-size:20px;color:var(--navy);font-weight:300}
.services-title strong{font-size:27px;font-weight:700}
.services-sub{font-size:13px;font-weight:300;color:var(--navy);margin-top:4px}
.services-tag{font-size:14px;font-weight:700;color:var(--teal);margin-top:2px}
.service{position:absolute;top:546px;width:160px;text-align:center}
.service-icon{width:148px;height:148px;margin:0 auto}
.service h3{font-size:11.5px;font-weight:700;color:var(--navy);line-height:14px;margin-top:16px}
.service p{font-size:9.5px;line-height:11px;color:var(--muted);margin-top:6px;font-weight:300}
.service a{display:inline-block;font-size:10px;font-weight:700;color:var(--navy);margin-top:6px}

/* footer */
.site-footer{position:absolute;top:830px;left:0;width:1200px;height:176px}
.footer-bg{position:absolute;top:0;left:0}
.footer-col{position:absolute;top:47px;color:#fff}
.footer-col h4{font-size:14px;font-weight:700;padding-bottom:2px;border-bottom:1px dotted #9cc6d8;display:inline-block;padding-right:20px}
.footer-col ul{list-style:none;margin-top:6px;font-size:12px;line-height:17px;font-weight:300}
.about h4{padding-left:8px;padding-right:20px}
.about-body{display:flex;gap:16px;margin-top:10px}
.about-mark{width:50px;height:50px;border-radius:50%;background:#fff;flex:none}
.about-body p{font-size:9.5px;line-height:11.5px;width:160px;font-weight:300}
.footer-bar{position:absolute;left:197px;top:154px;font-size:10px;color:#fff;font-weight:300}
</style>
</head>
<body>
<div class="page">

<header class="site-header">
  <div class="brand"><span class="brand-dot"></span><span class="brand-name">Vantrel Media</span></div>
  <div class="social"><span></span><span></span><span></span></div>
  <div class="search"><div class="search-field">CLICK TO SEARCH</div><div class="search-btn">SEARCH</div></div>
  <nav class="main-nav">
    <a class="active">HOME</a><a>FEATURES</a><a>OUR CUSTOMERS</a><a>PRICING</a><a>BLOG</a><a>CONTACT</a>
  </nav>
</header>

<section class="hero">
  <div class="hero-photo" role="img" aria-label="Photo of a smiling consultant in a dark suit with arms crossed"></div>
  <h1 class="hero-title"><strong>VANTREL MEDIA</strong> IS FORMED TO PROVIDE<br>CONSULTING &amp;CONTRACT SERVICES.</h1>
  <p class="hero-text">Vantrel Media was formed to provide consulting and contract services on a wide range of business tasks. We can be engaged for work on anything from half day to several month projects.</p>
  <div class="hero-actions"><span class="btn">REGISTERD NOW</span><span class="btn">GET A QUOTE</span></div>
  <svg class="hero-curve" width="1200" height="70" viewBox="0 0 1200 70">
    <path d="M0 70 L0 66 Q300 20 580 18 Q600 8 620 18 Q900 20 1200 66 L1200 70 Z" fill="#fff"/>
    <circle cx="600" cy="24" r="12" fill="var(--teal)"/>
  </svg>
</section>

<section class="services">
  <div class="services-head">
    <div class="rule"></div>
    <h2 class="services-title"><strong>SERVICES</strong> / WHAT WE DO</h2>
    <p class="services-sub">Lorem ipsum dolor sit amet, consectetuer ipsum dolor</p>
    <p class="services-tag">NONUMMY NIBH EUISMOD</p>
  </div>

  <div class="service" style="left:235px">
    <svg class="service-icon" viewBox="0 0 148 148">
      <circle cx="74" cy="74" r="72" fill="var(--red)"/><circle cx="74" cy="74" r="65" fill="none" stroke="#fff" stroke-width="3"/>
      <path d="M52 100 L82 70" stroke="#fff" stroke-width="12" stroke-linecap="round"/>
      <circle cx="90" cy="60" r="16" fill="#fff"/><circle cx="98" cy="52" r="7" fill="var(--red)"/>
      <circle cx="52" cy="100" r="3" fill="var(--red)"/>
    </svg>
    <h3>SOFTWARE<br>IMPLEMENTATION</h3>
    <p>Lorem ipsum dolor sit amet, consectetuer adipiscing elit, sed diam nonummy nibh euismod.</p>
    <a>READ MORE</a>
  </div>

  <div class="service" style="left:425px">
    <svg class="service-icon" viewBox="0 0 148 148">
      <circle cx="74" cy="74" r="72" fill="var(--teal)"/><circle cx="74" cy="74" r="65" fill="none" stroke="#fff" stroke-width="3"/>
      <circle cx="62" cy="62" r="12" fill="#fff"/><circle cx="88" cy="62" r="12" fill="#fff"/>
      <circle cx="75" cy="70" r="13" fill="#fff" stroke="var(--teal)" stroke-width="3"/>
      <path d="M52 106 Q52 86 75 86 Q98 86 98 106 Z" fill="#fff" stroke="var(--teal)" stroke-width="3"/>
    </svg>
    <h3>PROJECT<br>MANAGEMENT</h3>
    <p>Lorem ipsum dolor sit amet, consectetuer adipiscing elit, sed diam nonummy nibh euismod.</p>
    <a>READ MORE</a>
  </div>

  <div class="service" style="left:615px">
    <svg class="service-icon" viewBox="0 0 148 148">
      <circle cx="74" cy="74" r="72" fill="var(--navy)"/><circle cx="74" cy="74" r="65" fill="none" stroke="#fff" stroke-width="3"/>
      <g fill="#fff"><rect x="44" y="84" width="10" height="24"/><rect x="58" y="76" width="10" height="32"/><rect x="72" y="80" width="10" height="28"/><rect x="86" y="70" width="10" height="38"/><rect x="100" y="66" width="10" height="42"/></g>
      <polyline points="46,72 62,60 78,66 94,54 106,48" fill="none" stroke="#fff" stroke-width="4"/>
      <circle cx="106" cy="48" r="4" fill="#fff"/>
    </svg>
    <h3>PROJECT ANALYSIS<br>&amp; PLANNING</h3>
    <p>Lorem ipsum dolor sit amet, consectetuer adipiscing elit, sed diam nonummy nibh euismod.</p>
    <a>READ MORE</a>
  </div>

  <div class="service" style="left:805px">
    <svg class="service-icon" viewBox="0 0 148 148">
      <circle cx="74" cy="74" r="72" fill="var(--orange)"/><circle cx="74" cy="74" r="65" fill="none" stroke="#fff" stroke-width="3"/>
      <circle cx="62" cy="88" r="18" fill="none" stroke="#fff" stroke-width="9" stroke-dasharray="7 4"/>
      <circle cx="62" cy="88" r="13" fill="#fff"/><circle cx="62" cy="88" r="5" fill="var(--orange)"/>
      <circle cx="94" cy="58" r="13" fill="none" stroke="#fff" stroke-width="7" stroke-dasharray="5 3"/>
      <circle cx="94" cy="58" r="9" fill="#fff"/><circle cx="94" cy="58" r="4" fill="var(--orange)"/>
    </svg>
    <h3>BUSINESS PROCESS<br>ANALYSIS</h3>
    <p>Lorem ipsum dolor sit amet, consectetuer adipiscing elit, sed diam nonummy nibh euismod.</p>
    <a>READ MORE</a>
  </div>
</section>

<footer class="site-footer">
  <svg class="footer-bg" width="1200" height="176" viewBox="0 0 1200 176">
    <defs><linearGradient id="fg" x1="0" x2="1"><stop offset="0" stop-color="#1a6d95"/><stop offset=".5" stop-color="#14577a"/><stop offset="1" stop-color="#1a6d95"/></linearGradient></defs>
    <path d="M0 38 Q600 -38 1200 38 L1200 176 L0 176 Z" fill="url(#fg)"/>
  </svg>
  <div class="footer-col about" style="left:195px">
    <h4>ABOUT US</h4>
    <div class="about-body"><span class="about-mark"></span>
      <p>Lorem ipsum dolor sit amet, consectetuer adipiscing elit, sed diam nonummy nibh euismod tincidunt ut laoreet dolore magna</p></div>
  </div>
  <div class="footer-col" style="left:518px"><h4>LINKS</h4><ul><li>Company</li><li>Team</li><li>Careers</li><li>Contact us</li></ul></div>
  <div class="footer-col" style="left:682px"><h4>OTHER STUFF</h4><ul><li>Privacy Policy</li><li>Terms of</li><li>Service</li><li>Sitemap</li></ul></div>
  <div class="footer-col" style="left:864px"><h4>CONTACT US</h4><ul><li>48 Holloway Lane</li><li>Suite 7</li><li>Marbury, DE 19822 US</li><li>Carrer de Lluna 9, 3-1</li><li>08012 Tarvella, Spain</li></ul></div>
  <div class="footer-bar">Home | About Us | Patent Pending | Copy Right | Privacy | Contact Us Privacy</div>
</footer>

</div>
</body>
</html>
```